Marlow Landscaping

Create a website for a new landscaping company. I have a logo already and description of services offered. I have a website that I would like all inquiries and appointments to get forwarded to. I need just need it well organized so that a husband and wife team can manage it easily. This is a company that will continue to grow over time and will need to add more services under new tabs over time. If you need the email where appointments and inquiries should go please send me a message.
Services offered are: Weekly/bi weekly mowing, weed eating and edging, Plant installation pinestraw & mulch installation, weed & feed, leaf removal and yard clean up.

```html
<!DOCTYPE html>
<html lang="en">
<head>
<meta charset="utf-8">
<title>Marlow Landscaping</title>
<link rel="stylesheet" href="https://fonts.googleapis.com/css2?family=Montserrat:wght@400;500;600;700;800&family=Open+Sans:wght@400;600&display=swap">
<style>
:root{
  --green:#5f9a2a;
  --green-dark:#3e7a1d;
  --green-light:#8cc041;
  --orange:#e9a531;
  --orange-dark:#d98e1c;
  --ink:#1f1f1f;
  --text:#4a4a4a;
  --white:#ffffff;
  --cream:#fbf6ea;
  --field:#ffffff;
}
*{box-sizing:border-box;margin:0;padding:0}
html,body{width:1200px;height:4808px;overflow:hidden}
body{font-family:"Open Sans",sans-serif;color:var(--text);background:var(--white);position:relative}
.section{position:absolute;left:0;width:1200px;overflow:hidden}
.photo{position:absolute;border-radius:16px}
.btn{position:absolute;display:flex;align-items:center;justify-content:center;border-radius:30px;font-family:"Montserrat",sans-serif;font-weight:700;font-size:15px;letter-spacing:.5px;text-transform:uppercase}
.btn-orange{background:var(--orange);color:var(--white)}
.btn-white{background:var(--white);color:var(--orange)}
.heading{position:absolute;left:0;width:1200px;text-align:center;font-family:"Montserrat",sans-serif;font-weight:800;font-size:46px;color:var(--ink);text-transform:uppercase}
.brand-name{font-family:"Montserrat",sans-serif;font-weight:800;color:var(--green-dark);text-transform:uppercase}

/* header */
.site-header{top:0;height:150px;background:var(--white);z-index:5;border-bottom-right-radius:0}
.logo{position:absolute;left:36px;top:28px;display:flex;align-items:center;gap:12px}
.logo-dot{width:44px;height:44px;border-radius:50%;background:var(--green)}
.logo .brand-name{font-size:26px;line-height:1.05}
.header-phone{position:absolute;left:770px;top:22px;display:flex;align-items:center;gap:10px;font-family:"Montserrat",sans-serif}
.header-phone small{display:block;font-size:12px;color:var(--text)}
.header-phone b{font-size:22px;color:var(--ink)}
.icon-circle{width:40px;height:40px;border-radius:50%;background:var(--orange);display:flex;align-items:center;justify-content:center}
.nav{position:absolute;left:415px;top:96px;display:flex;gap:34px;font-family:"Montserrat",sans-serif;font-weight:700;font-size:16px;color:var(--ink)}
.nav .active{color:var(--orange)}
.socials{position:absolute;display:flex;gap:12px}
.social{width:34px;height:34px;border-radius:50%;background:#eeeeee}
.social.on{background:var(--orange)}

/* hero */
.hero{top:0;height:820px}
.hero-photo{position:absolute;inset:0;background:linear-gradient(180deg,#4c6b35 0%,#6f8f46 40%,#49712a 100%)}
.hero-shade{position:absolute;inset:0;background:linear-gradient(90deg,rgba(20,30,10,.35),rgba(20,30,10,.15))}
.hero h1{position:absolute;top:282px;left:0;width:1200px;text-align:center;font-family:"Montserrat",sans-serif;font-weight:800;font-size:50px;line-height:1.12;color:var(--white)}
.hero p{position:absolute;top:408px;left:0;width:1200px;text-align:center;font-family:"Montserrat",sans-serif;font-weight:700;font-size:22px;line-height:1.35;color:var(--white)}
.hero .btn{left:470px;top:470px;width:260px;height:50px}
.hero-dots{position:absolute;right:30px;top:395px;display:flex;flex-direction:column;gap:14px}
.hero-dots i{width:10px;height:10px;border-radius:50%;background:rgba(255,255,255,.6)}
.hero-dots i:first-child{background:var(--white)}

/* about */
.about{top:770px;height:620px;background:linear-gradient(135deg,var(--green-light),var(--green) 55%,var(--green-dark))}
.about h2{position:absolute;left:110px;top:80px;font-family:"Montserrat",sans-serif;font-weight:800;font-size:46px;color:var(--white)}
.about-bar{position:absolute;left:110px;top:138px;width:170px;height:3px;background:var(--white)}
.about p{position:absolute;left:110px;width:520px;font-size:16px;line-height:1.6;color:var(--white)}
.about .btn{left:110px;top:452px;width:150px;height:46px}
.about-call{position:absolute;left:290px;top:450px;display:flex;align-items:center;gap:10px;color:var(--white);font-family:"Montserrat",sans-serif}
.about-call small{display:block;font-size:12px}
.about-call b{font-size:20px}
.about-ring{position:absolute;left:636px;top:42px;width:450px;height:450px;border-radius:50%;border:10px solid rgba(255,255,255,.85)}
.about-photo{position:absolute;left:646px;top:52px;width:430px;height:430px;border-radius:50%;background:radial-gradient(circle at 45% 40%,#9bbf6a,#4f7b2c 75%)}
.about-photo-small{position:absolute;left:620px;top:310px;width:185px;height:185px;border-radius:50%;border:7px solid var(--white);background:radial-gradient(circle,#b59a6a,#6c7d3e 80%)}

/* services */
.services{top:1365px;height:820px;background:var(--white)}
.services .heading{top:102px}
.heading-bar{position:absolute;left:545px;width:110px;height:3px;background:var(--orange)}
.card{position:absolute;top:200px;width:320px;height:490px;background:var(--white);border-radius:16px;box-shadow:0 8px 26px rgba(0,0,0,.12);overflow:hidden}
.card-photo{position:absolute;left:0;top:0;width:320px;height:240px}
.card-icon{position:absolute;left:125px;top:178px;width:70px;height:70px;border-radius:50%;background:var(--white);border:3px solid var(--green);display:flex;align-items:center;justify-content:center}
.card.featured .card-icon{background:var(--green)}
.card h3{position:absolute;top:272px;left:0;width:320px;text-align:center;font-family:"Montserrat",sans-serif;font-weight:800;font-size:17px;color:var(--ink);text-transform:uppercase}
.card p{position:absolute;top:308px;left:40px;width:240px;text-align:center;font-size:14px;line-height:1.55;color:var(--text)}
.card .btn{left:90px;top:412px;width:140px;height:42px;font-size:13px;box-shadow:0 3px 10px rgba(0,0,0,.1)}
.arrow{position:absolute;top:430px}

/* why */
.why{top:2165px;height:660px;background:linear-gradient(135deg,#f1b545,var(--orange) 50%,var(--orange-dark))}
.why .heading{top:62px;color:var(--white);font-weight:500}
.why-label{position:absolute;font-family:"Montserrat",sans-serif;font-weight:700;font-size:15px;color:var(--white);text-transform:uppercase;line-height:1.35}
.why-node{position:absolute;width:64px;height:64px;border-radius:50%;background:var(--white);display:flex;align-items:center;justify-content:center}
.why-node.on{background:var(--green)}
.why-center{position:absolute;left:470px;top:335px;width:260px;height:260px;border-radius:50%;background:var(--white);border:8px solid #f6d48c;display:flex;flex-direction:column;align-items:center;justify-content:center;gap:10px}
.why-center .brand-name{font-size:30px}
.why-center small{font-family:"Montserrat",sans-serif;font-size:13px;color:var(--ink)}

/* works */
.works{top:2810px;height:890px;background:var(--white)}
.works .heading{top:50px}
.works .btn{left:485px;top:765px;width:230px;height:54px}

/* contact */
.contact{top:3690px;height:780px;background:linear-gradient(160deg,#7fae3e,var(--green) 50%,#3f7a22)}
.contact .heading{top:100px;color:var(--white)}
.info{position:absolute;top:195px;display:flex;gap:12px;color:var(--white);font-family:"Montserrat",sans-serif;font-size:14px;line-height:1.4}
.info b{display:block;font-size:14px}
.info .ic{width:50px;height:50px;border-radius:50%;border:2px solid var(--orange);display:flex;align-items:center;justify-content:center;flex:none}
.field{position:absolute;width:440px}
.field label{display:block;font-family:"Montserrat",sans-serif;font-size:15px;color:var(--white);margin-bottom:6px}
.field .input{height:46px;background:var(--field);border-radius:4px;font-size:14px;color:#9a9a9a;padding:13px 16px}
.field.wide{width:910px}
.field.wide .input{height:86px}
.contact .btn{left:515px;top:578px;width:170px;height:48px}

/* footer */
.footer{top:4455px;height:353px;background:linear-gradient(180deg,var(--white),var(--cream))}
.footer-logo{position:absolute;left:66px;top:80px;display:flex;flex-direction:column;align-items:center;gap:10px;width:220px}
.footer-logo .logo-dot{width:60px;height:60px}
.footer-logo .brand-name{font-size:24px;text-align:center;line-height:1.1}
.footer-col{position:absolute;top:70px;font-family:"Montserrat",sans-serif}
.footer-col h4{font-size:18px;font-weight:800;color:var(--ink);text-transform:uppercase;margin-bottom:16px}
.footer-col li{list-style:none;font-size:14px;color:var(--text);margin-bottom:14px;display:flex;align-items:center;gap:10px}
.footer-col li i{width:8px;height:8px;border-radius:50%;background:var(--orange);display:inline-block}
.contact-line{font-size:13px;color:var(--text);margin-bottom:12px;line-height:1.4;display:flex;gap:8px}
.contact-line b{display:block;color:var(--ink)}
.news{position:absolute;top:112px;left:0;width:300px;height:46px;border-radius:24px;background:var(--white);box-shadow:0 2px 8px rgba(0,0,0,.1);font-size:13px;color:#999;padding:14px 18px}
.news .btn{left:190px;top:0;width:110px;height:46px;font-size:13px}
.bottom-bar{position:absolute;left:0;top:4748px;width:1200px;height:60px;background:#f3ecd8;display:flex;align-items:center;justify-content:center;font-size:13px;color:var(--text)}
</style>
</head>
<body>

<!-- hero -->
<section class="section hero">
  <div class="hero-photo" role="img" aria-label="Landscaper pushing a lawn mower across a green lawn beside garden beds"></div>
  <div class="hero-shade"></div>
  <h1>PROFESSIONAL LAWN CARE<br>YOU CAN COUNT ON</h1>
  <p>Veteran Owned &amp; Operated • Fully Licensed &amp; Insured<br>• Reliable, Affordable Service</p>
  <div class="btn btn-orange">Schedule an Appointment</div>
  <div class="hero-dots"><i></i><i></i><i></i></div>
  <svg style="position:absolute;left:0;bottom:0" width="1200" height="120" viewBox="0 0 1200 120"><path d="M0 120 L0 40 Q600 150 1200 40 L1200 120 Z" fill="#ffffff"/></svg>
</section>

<!-- header -->
<header class="section site-header">
  <div class="logo"><span class="logo-dot"></span><span class="brand-name">Marlow<br>Landscaping</span></div>
  <div class="header-phone">
    <span class="icon-circle"><svg width="18" height="18" viewBox="0 0 24 24"><path d="M6.6 10.8a15 15 0 0 0 6.6 6.6l2.2-2.2a1 1 0 0 1 1-.25 11.4 11.4 0 0 0 3.6.57 1 1 0 0 1 1 1V20a1 1 0 0 1-1 1A17 17 0 0 1 3 4a1 1 0 0 1 1-1h3.5a1 1 0 0 1 1 1c0 1.25.2 2.45.57 3.57a1 1 0 0 1-.25 1z" fill="#fff"/></svg></span>
    <span><small>Call Us</small><b>(555) 014 2290</b></span>
  </div>
  <div class="btn btn-orange" style="left:1000px;top:20px;width:160px;height:48px">Get a Quote</div>
  <nav class="nav"><span class="active">HOME</span><span>ABOUT US</span><span>OUR SERVICES</span><span>PROJECTS</span><span>CONTACT</span></nav>
  <div class="socials" style="left:1052px;top:88px"><span class="social on"></span><span class="social"></span><span class="social"></span></div>
</header>

<!-- about -->
<section class="section about">
  <svg style="position:absolute;left:0;top:0" width="1200" height="60" viewBox="0 0 1200 60"><path d="M0 0 L1200 0 L1200 10 Q600 70 0 10 Z" fill="#ffffff"/></svg>
  <h2>ABOUT US</h2>
  <div class="about-bar"></div>
  <p style="top:170px">Marlow Lawn Care &amp; Landscaping was founded with a simple goal — provide dependable, high-quality lawn care that homeowners can trust. As a Veteran Owned &amp; Operated business, we bring discipline, reliability, and attention to detail to every job. Our team is fully licensed and insured, giving you peace of mind while we care for your property.</p>
  <p style="top:340px">Whether it's routine maintenance or a full yard transformation, we show up ready to work and committed to delivering results you'll love.</p>
  <div class="btn btn-orange">Learn More</div>
  <div class="about-call">
    <span class="icon-circle" style="background:#fff"><svg width="18" height="18" viewBox="0 0 24 24"><path d="M6.6 10.8a15 15 0 0 0 6.6 6.6l2.2-2.2a1 1 0 0 1 1-.25 11.4 11.4 0 0 0 3.6.57 1 1 0 0 1 1 1V20a1 1 0 0 1-1 1A17 17 0 0 1 3 4a1 1 0 0 1 1-1h3.5a1 1 0 0 1 1 1c0 1.25.2 2.45.57 3.57a1 1 0 0 1-.25 1z" fill="#e9a531"/></svg></span>
    <span><small>Call Us</small><b>(555) 014 2290</b></span>
  </div>
  <div class="about-ring"></div>
  <div class="about-photo" role="img" aria-label="Worker trimming the edge of a lawn with a string trimmer"></div>
  <div class="about-photo-small" role="img" aria-label="Close-up of a freshly edged lawn border"></div>
  <svg style="position:absolute;left:0;bottom:0" width="1200" height="80" viewBox="0 0 1200 80"><path d="M0 80 L0 60 Q600 -10 1200 60 L1200 80 Z" fill="#ffffff"/></svg>
</section>

<!-- services -->
<section class="section services">
  <h2 class="heading">Our Services</h2>
  <div class="heading-bar" style="top:162px"></div>
  <svg class="arrow" style="left:36px" width="22" height="34" viewBox="0 0 22 34"><path d="M18 3 L5 17 L18 31" stroke="#b5b5b5" stroke-width="5" fill="none"/></svg>
  <svg class="arrow" style="left:1142px" width="22" height="34" viewBox="0 0 22 34"><path d="M4 3 L17 17 L4 31" stroke="#3e7a1d" stroke-width="5" fill="none"/></svg>

  <div class="card" style="left:100px">
    <div class="card-photo" role="img" aria-label="Striped green lawn being mowed" style="background:linear-gradient(160deg,#8cba55,#4f7f2c)"></div>
    <div class="card-icon"><svg width="34" height="34" viewBox="0 0 34 34"><rect x="6" y="14" width="20" height="10" rx="2" fill="#3e7a1d"/><circle cx="10" cy="27" r="4" fill="#3e7a1d"/><circle cx="24" cy="27" r="4" fill="#3e7a1d"/><path d="M22 14 L30 4" stroke="#3e7a1d" stroke-width="3"/></svg></div>
    <h3>Weekly &amp; Bi-Weekly Mowing</h3>
    <p>Lorem ipsum dolor sit amet, consectetur adipiscing elit, sed do eiusmod tempores.</p>
    <div class="btn btn-white">Learn More</div>
  </div>
  <div class="card featured" style="left:440px">
    <div class="card-photo" role="img" aria-label="Worker edging a lawn along a walkway" style="background:linear-gradient(160deg,#9cc063,#5a8833)"></div>
    <div class="card-icon"><svg width="34" height="34" viewBox="0 0 34 34"><path d="M8 30 L26 6" stroke="#fff" stroke-width="3"/><path d="M4 28 Q10 22 14 30" stroke="#fff" stroke-width="3" fill="none"/></svg></div>
    <h3>Weed Eating and Hedging</h3>
    <p>Lorem ipsum dolor sit amet, consectetur adipiscing elit, sed do eiusmod tempores.</p>
    <div class="btn btn-orange">Learn More</div>
  </div>
  <div class="card" style="left:780px">
    <div class="card-photo" role="img" aria-label="Flower beds and shrubs planted in front of a house" style="background:linear-gradient(160deg,#a7c779,#5f8a3a)"></div>
    <div class="card-icon"><svg width="34" height="34" viewBox="0 0 34 34"><path d="M17 30 L17 14" stroke="#3e7a1d" stroke-width="3"/><path d="M17 16 Q8 14 7 5 Q16 6 17 16 Q18 6 27 5 Q26 14 17 16Z" fill="#3e7a1d"/><rect x="10" y="26" width="14" height="6" rx="2" fill="#3e7a1d"/></svg></div>
    <h3>Plant Installation</h3>
    <p>Lorem ipsum dolor sit amet, consectetur adipiscing elit, sed do eiusmod tempores.</p>
    <div class="btn btn-white">Learn More</div>
  </div>
</section>

<!-- why choose us -->
<section class="section why">
  <svg style="position:absolute;left:0;top:0" width="1200" height="60" viewBox="0 0 1200 60"><path d="M0 0 L1200 0 L1200 5 Q600 60 0 5 Z" fill="#ffffff"/></svg>
  <h2 class="heading">Why Choose Us</h2>
  <div class="heading-bar" style="top:120px;background:#fff"></div>
  <svg style="position:absolute;left:0;top:0" width="1200" height="660" viewBox="0 0 1200 660">
    <path d="M330 465 A270 270 0 0 1 870 465" stroke="#ffffff" stroke-width="3" fill="none"/>
    <path d="M390 465 A210 210 0 0 1 810 465" stroke="rgba(255,255,255,.5)" stroke-width="2" fill="none"/>
  </svg>
  <div class="why-label" style="left:0;width:1200px;text-align:center;top:172px">Affordable Pricing</div>
  <div class="why-node" style="left:568px;top:210px"><svg width="30" height="30" viewBox="0 0 30 30"><path d="M4 15 L15 4 L26 4 L26 15 L15 26 Z" fill="none" stroke="#5f9a2a" stroke-width="2.5"/><circle cx="20" cy="10" r="2" fill="#5f9a2a"/></svg></div>

  <div class="why-label" style="left:150px;top:288px">Fully Licensed &amp; Insured</div>
  <div class="why-node" style="left:380px;top:295px"><svg width="30" height="30" viewBox="0 0 30 30"><path d="M15 3 L25 7 L25 15 Q25 23 15 27 Q5 23 5 15 L5 7Z" fill="none" stroke="#5f9a2a" stroke-width="2.5"/><path d="M10 15 L14 19 L20 11" stroke="#5f9a2a" stroke-width="2.5" fill="none"/></svg></div>

  <div class="why-node on" style="left:756px;top:295px"><svg width="30" height="30" viewBox="0 0 30 30"><circle cx="11" cy="10" r="4" fill="#fff"/><circle cx="20" cy="10" r="4" fill="#fff"/><path d="M4 24 Q11 14 16 24 M14 24 Q20 14 27 24" stroke="#fff" stroke-width="2.5" fill="none"/></svg></div>
  <div class="why-label" style="left:838px;top:288px">Friendly, Professional<br>Service</div>

  <div class="why-label" style="left:150px;top:436px">Veteran Owned &amp;<br>Operated</div>
  <div class="why-node" style="left:318px;top:420px"><svg width="30" height="30" viewBox="0 0 30 30"><circle cx="15" cy="19" r="7" fill="none" stroke="#5f9a2a" stroke-width="2.5"/><path d="M10 4 L15 12 L20 4" stroke="#5f9a2a" stroke-width="2.5" fill="none"/></svg></div>

  <div class="why-node" style="left:818px;top:420px"><svg width="30" height="30" viewBox="0 0 30 30"><circle cx="15" cy="15" r="11" fill="none" stroke="#5f9a2a" stroke-width="2.5"/><path d="M15 8 L15 15 L20 18" stroke="#5f9a2a" stroke-width="2.5" fill="none"/></svg></div>
  <div class="why-label" style="left:900px;top:442px">Reliable &amp; On-Time</div>

  <div class="why-center"><span class="logo-dot" style="width:46px;height:46px;border-radius:50%;background:var(--green)"></span><span class="brand-name">Marlow</span><small>(555) 014 2290</small></div>
  <svg style="position:absolute;left:0;bottom:0" width="1200" height="110" viewBox="0 0 1200 110"><path d="M0 110 L0 80 Q600 -20 1200 80 L1200 110Z" fill="#ffffff"/><path d="M0 80 Q600 -20 1200 80" stroke="#5f9a2a" stroke-width="6" fill="none"/></svg>
</section>

<!-- works -->
<section class="section works">
  <h2 class="heading">See Our Works</h2>
  <div class="photo" style="left:112px;top:120px;width:478px;height:300px;background:linear-gradient(150deg,#7aa84a,#3f6a25)" role="img" aria-label="Curved garden bed with hostas bordering a lawn"></div>
  <div class="photo" style="left:610px;top:120px;width:478px;height:300px;background:linear-gradient(150deg,#94b85c,#567f31)" role="img" aria-label="Landscaper mowing a wide green lawn"></div>
  <div class="photo" style="left:112px;top:432px;width:312px;height:290px;background:linear-gradient(150deg,#a6bf5e,#5b7d2e)" role="img" aria-label="Worker trimming grass near yellow flowers"></div>
  <div class="photo" style="left:444px;top:432px;width:312px;height:290px;background:linear-gradient(150deg,#9a8e6a,#586d32)" role="img" aria-label="Wheelbarrow with garden tools and plants"></div>
  <div class="photo" style="left:776px;top:432px;width:312px;height:290px;background:linear-gradient(150deg,#9fc36f,#4b7a2c)" role="img" aria-label="Landscaped backyard with stone path and shrubs"></div>
  <div class="btn btn-orange">View More Works</div>
</section>

<!-- contact -->
<section class="section contact" role="img" aria-label="Green lawn background behind the contact form">
  <svg style="position:absolute;left:0;top:0" width="1200" height="60" viewBox="0 0 1200 60"><path d="M0 0 L1200 0 L1200 10 Q600 70 0 10 Z" fill="#ffffff"/></svg>
  <h2 class="heading">Get in Touch</h2>
  <div class="heading-bar" style="top:162px;background:#fff"></div>
  <div class="info" style="left:200px"><span class="ic"><svg width="22" height="22" viewBox="0 0 24 24"><path d="M12 2a7 7 0 0 0-7 7c0 5 7 13 7 13s7-8 7-13a7 7 0 0 0-7-7zm0 9.5a2.5 2.5 0 1 1 0-5 2.5 2.5 0 0 1 0 5z" fill="#e9a531"/></svg></span><span><b>LOCATION:</b>465, Lorem Ipsum Grove Rd,<br>United States</span></div>
  <div class="info" style="left:510px"><span class="ic"><svg width="20" height="20" viewBox="0 0 24 24"><path d="M6.6 10.8a15 15 0 0 0 6.6 6.6l2.2-2.2a1 1 0 0 1 1-.25 11.4 11.4 0 0 0 3.6.57 1 1 0 0 1 1 1V20a1 1 0 0 1-1 1A17 17 0 0 1 3 4a1 1 0 0 1 1-1h3.5a1 1 0 0 1 1 1c0 1.25.2 2.45.57 3.57a1 1 0 0 1-.25 1z" fill="#e9a531"/></svg></span><span><b>PHONE:</b>(555) 014 2290</span></div>
  <div class="info" style="left:750px"><span class="ic"><svg width="22" height="22" viewBox="0 0 24 24"><rect x="3" y="5" width="18" height="14" rx="2" fill="none" stroke="#e9a531" stroke-width="2"/><path d="M3 7 L12 13 L21 7" stroke="#e9a531" stroke-width="2" fill="none"/></svg></span><span><b>EMAIL:</b>info@marlowlandscaping.example</span></div>

  <div class="field" style="left:140px;top:280px"><label>First Name:</label><div class="input">Enter Your First Name</div></div>
  <div class="field" style="left:610px;top:280px"><label>Last Name:</label><div class="input">Enter Your Last Name</div></div>
  <div class="field" style="left:140px;top:372px"><label>Phone:</label><div class="input">Enter Phone Number</div></div>
  <div class="field" style="left:610px;top:372px"><label>Email:</label><div class="input">Enter Email Address</div></div>
  <div class="field wide" style="left:140px;top:464px"><label>Message:</label><div class="input">Enter Comments</div></div>
  <div class="btn btn-orange">Send Message</div>
  <svg style="position:absolute;left:0;bottom:0" width="1200" height="90" viewBox="0 0 1200 90"><path d="M0 90 L0 70 Q600 -10 1200 70 L1200 90Z" fill="#ffffff"/></svg>
</section>

<!-- footer -->
<footer class="section footer">
  <div class="footer-logo"><span class="logo-dot"></span><span class="brand-name">Marlow<br>Landscaping</span></div>
  <div class="footer-col" style="left:345px">
    <h4>Quick Links</h4>
    <ul><li><i></i>Home</li><li><i></i>About Us</li><li><i></i>Our Services</li><li><i></i>Projects</li><li><i></i>Contact</li></ul>
  </div>
  <div class="footer-col" style="left:530px;width:220px">
    <h4>Contact Info</h4>
    <div class="contact-line"><span><b>ADDRESS:</b>465 Lorem Ipsum Grove, United States</span></div>
    <div class="contact-line"><span><b>PHONE:</b>(555) 014 2290</span></div>
    <div class="contact-line"><span><b>EMAIL:</b>info@marlowlandscaping.example</span></div>
  </div>
  <div class="footer-col" style="left:780px;width:310px">
    <h4>Newsletter Signup</h4>
    <div class="news">Email Address<div class="btn btn-orange">Sign Up</div></div>
  </div>
</footer>
<div class="bottom-bar">© 2026 Marlow Landscaping · All Rights Reserved</div>
<div class="socials" style="left:952px;top:4761px"><span class="social on"></span><span class="social" style="background:#fff"></span><span class="social" style="background:#fff"></span></div>

</body>
</html>
```